VENTO SAURELLE

Project name: “Vento Saurelle” website
Objective: To create an elegant website,
intuitive and responsive to present this
what is “Vento Saurelle”
See attached specifications.

```html
<!DOCTYPE html>
<html lang="en">
<head>
<meta charset="utf-8">
<title>Vento Saurelle</title>
<link href="https://fonts.googleapis.com/css2?family=Gilda+Display&family=Inter:wght@400;500;600&display=swap" rel="stylesheet">
<style>
:root{
  --forest:#2f4a2d;
  --forest-deep:#263d25;
  --sage:#94ac93;
  --sage-light:#a6bca5;
  --ink:#263326;
  --ink-soft:#334233;
  --white:#ffffff;
  --card-line:#5d735c;
  --divider:#6f856e;
}
*{box-sizing:border-box;margin:0;padding:0}
html,body{width:1200px;height:4651px;overflow:hidden}
body{position:relative;background:var(--sage);color:var(--ink);font-family:"Inter",sans-serif}
.abs{position:absolute}
.center{text-align:center;left:0;width:1200px}

/* header */
.site-header{position:absolute;left:0;top:0;width:1200px;height:126px;background:var(--forest)}
.brand{position:absolute;display:flex;flex-direction:column;align-items:center;gap:8px;color:var(--white);font-family:"Inter",sans-serif;font-weight:600;letter-spacing:2px}
.brand-dot{border:2px solid var(--white);border-radius:50%}
.site-header .brand{left:150px;top:20px;font-size:13px}
.site-header .brand-dot{width:58px;height:58px}
.main-nav a{position:absolute;top:44px;color:var(--white);text-decoration:none;font-family:"Gilda Display",serif;font-size:18px}
.main-nav .active{border-bottom:1px solid var(--white);border-top:1px solid var(--white);padding:4px 6px;top:38px}
.nav-contact{left:848px;top:36px !important;width:94px;height:45px;background:#8ea38c;display:flex;align-items:center;justify-content:center}
.lang{position:absolute;left:960px;top:36px;width:90px;height:45px;border:1px solid #b7c6b6;color:var(--white);font-family:"Gilda Display",serif;font-size:16px;display:flex;align-items:center;justify-content:center;gap:8px}
.lang-dot{width:12px;height:12px;border-radius:50%;background:#c9807a}

/* hero */
.hero{position:absolute;left:0;top:126px;width:1200px;height:484px;background:linear-gradient(180deg,#5f7a4a 0%,#8a9461 35%,#a89a6e 55%,#4f6b36 80%,#3d5a2b 100%)}
.hero h1{position:absolute;top:134px;left:0;width:1200px;text-align:center;font-family:"Gilda Display",serif;font-weight:400;font-size:64px;color:var(--white)}
.hero p{position:absolute;top:226px;left:0;width:1200px;text-align:center;font-size:18px;font-weight:500;color:var(--white)}
.btn{position:absolute;display:flex;align-items:center;justify-content:center;background:var(--white);color:var(--ink);font-family:"Gilda Display",serif;font-size:20px;height:54px;text-decoration:none}
.btn-dark{background:var(--forest);color:var(--white);font-size:17px}

.photo{position:absolute;border-radius:50%;border:2px solid var(--forest-deep)}

/* neutral stand-in for the wavy ornament */
.divider{position:absolute;width:96px;height:10px;border-radius:5px;background:var(--divider)}
h2.section-title{position:absolute;font-family:"Gilda Display",serif;font-weight:400;font-size:40px;color:var(--ink)}
.lead{position:absolute;font-size:14.5px;line-height:23px;color:var(--ink)}

/* welcome */
.welcome-copy{position:absolute;left:655px;top:682px;width:390px}
.welcome-copy .kicker{font-family:"Gilda Display",serif;font-size:25px}
.welcome-copy h2{font-family:"Gilda Display",serif;font-weight:400;font-size:50px;line-height:60px}
.welcome-copy .divider{position:relative;display:block;margin:6px 0 36px}
.welcome-copy p{font-size:14.5px;line-height:23px;margin-bottom:17px}

/* discover */
.spot{position:absolute;width:320px;text-align:center}
.spot h3{font-family:"Gilda Display",serif;font-weight:400;font-size:19px;color:var(--ink);margin-bottom:10px}
.spot p{font-size:12.5px;line-height:18px;color:var(--ink-soft)}

/* reviews */
.review{position:absolute;top:2635px;width:202px;height:288px;border:1.5px solid var(--card-line);border-top:none;padding:20px 26px 0 26px}
.review .q{position:absolute;font-family:"Gilda Display",serif;font-size:40px;color:var(--ink-soft);line-height:1}
.review .stars{font-size:15px;letter-spacing:2px;color:var(--ink-soft);margin-top:6px}
.review p{font-size:10.5px;line-height:16px;margin-top:8px;color:var(--ink-soft)}
.reviewer{display:flex;align-items:center;gap:10px;margin-top:18px}
.avatar{width:40px;height:40px;border-radius:50%;background:#9aa05c}
.reviewer b{display:block;font-family:"Gilda Display",serif;font-weight:400;font-size:14px}
.reviewer small{font-size:10px}
.arrow{position:absolute;top:2762px}

/* posts */
.feed{position:absolute;left:152px;top:3281px;width:898px;height:361px;background:var(--forest);padding:7px;display:flex;gap:7px}
.post{flex:1;background:var(--white);position:relative;font-size:13px;color:#1c1e21}
.post-head{display:flex;align-items:center;gap:8px;padding:12px 14px 0}
.post-head .dot{width:30px;height:30px;border-radius:50%;border:1.5px solid #555}
.post-head b{font-size:11px;letter-spacing:1px}
.post-head .follow{color:#3b6fd3;font-size:10px}
.post-head .x{margin-left:auto;font-size:15px}
.post-text{padding:10px 16px;font-size:12.5px;line-height:18px;height:66px}
.post-photo{height:158px}
.post-foot{padding:8px 12px;font-size:10px;color:#555}
.post-actions{display:flex;justify-content:space-around;font-size:10px;color:#555;margin-top:10px}

/* cta */
.cta{position:absolute;left:0;top:3727px;width:1200px;height:491px;background:var(--forest)}
.cta h2{position:absolute;top:212px;left:0;width:1200px;text-align:center;font-family:"Gilda Display",serif;font-weight:400;font-size:40px;color:var(--white)}
.cta p{position:absolute;top:286px;left:0;width:1200px;text-align:center;font-size:17px;line-height:28px;color:#d4ddd3}
.cta-mark{position:absolute;left:542px;top:65px;width:116px;height:116px;border:3px solid var(--white);border-radius:50%}

/* footer */
.footer-mark{position:absolute;left:537px;top:4280px;width:126px;height:126px;border:3px solid var(--forest);border-radius:50%}
.footer-name{position:absolute;top:4422px;left:0;width:1200px;text-align:center;font-weight:600;font-size:28px;letter-spacing:4px;color:var(--forest)}
.footer-nav a{position:absolute;top:4495px;font-family:"Gilda Display",serif;font-size:18px;color:var(--ink);text-decoration:none}
.copyright{position:absolute;top:4560px;left:0;width:1200px;text-align:center;font-family:"Gilda Display",serif;font-size:14px}
</style>
</head>
<body>

<header class="site-header">
  <div class="brand"><span class="brand-dot"></span>VENTO SAURELLE</div>
  <nav class="main-nav">
    <a class="active" style="left:426px">Home</a>
    <a style="left:533px">About Us</a>
    <a style="left:666px">Land Prospecting</a>
    <a class="nav-contact">Contact</a>
  </nav>
  <div class="lang"><span class="lang-dot"></span>En ▾</div>
</header>

<section class="hero" role="img" aria-label="Aerial view of rolling Limousin farmland, fields and forests">
  <h1>Discover the Authentic Limousin</h1>
  <p>Nature, space, and serenity — let us guide you to your future land in the heart of France.</p>
  <a class="btn" style="left:383px;top:289px;width:243px">Discover Our Actions</a>
  <a class="btn" style="left:650px;top:289px;width:166px">Contact Us</a>
</section>

<section class="welcome">
  <div class="photo" role="img" aria-label="Medieval village with stone church tower among trees" style="left:158px;top:707px;width:434px;height:434px;background:radial-gradient(circle at 50% 45%,#8a7d6a,#5f6e45 60%,#3e5330)"></div>
  <div class="welcome-copy">
    <div class="kicker">Welcome to</div>
    <h2>Vento Saurelle</h2>
    <span class="divider" role="img" aria-label="Wavy ornamental divider"></span>
    <p>At Vento Saurelle, we promote the beauty and potential of the Limousin region.</p>
    <p>Our mission is to connect families, couples, and professionals with the perfect piece of land—whether for living, investing, or creating a rural project.</p>
    <p>With our local expertise and network, we simplify the search for land and highlight what makes this region so unique.</p>
    <a class="btn btn-dark" style="position:relative;width:127px;height:47px;margin-top:22px">Read More</a>
  </div>
</section>

<section class="discover">
  <h2 class="section-title center" style="top:1258px">What to Discover in Limousin</h2>
  <p class="lead center" style="top:1324px">The Limousin offers a rare harmony between nature and culture. Explore a selection of<br>activities for families, outdoor lovers, and curious travelers.</p>
  <span class="divider" role="img" aria-label="Wavy ornamental divider" style="left:552px;top:1397px"></span>

  <div class="photo" role="img" aria-label="Castle on a lake shore" style="left:153px;top:1480px;width:260px;height:260px;background:radial-gradient(circle,#7c7a5a,#4d6a3a 60%,#5f83a0)"></div>
  <div class="photo" role="img" aria-label="Hiking trail through a green forest" style="left:467px;top:1480px;width:260px;height:260px;background:radial-gradient(circle,#5c7b4a,#3e5f33 70%)"></div>
  <div class="photo" role="img" aria-label="Plate of local food with fries and grilled meat" style="left:787px;top:1480px;width:260px;height:260px;background:radial-gradient(circle,#c9a06a,#8b5438 60%,#5b4638)"></div>
  <div class="spot" style="left:123px;top:1786px"><h3>Lakes &amp; Water Activities</h3><p>Enjoy swimming, kayaking, paddle<br>boarding, and lakeside relaxation.</p></div>
  <div class="spot" style="left:437px;top:1786px"><h3>Hiking Trails &amp; Forest Walks</h3><p>Discover preserved landscapes and<br>peaceful routes for all levels.</p></div>
  <div class="spot" style="left:757px;top:1786px"><h3>Local Gastronomy</h3><p>Taste the authentic Limousin beef,<br>chestnuts, and artisanal products.</p></div>

  <div class="photo" role="img" aria-label="Historic stone village by a river" style="left:153px;top:1940px;width:260px;height:260px;background:radial-gradient(circle,#b8ad92,#6f7e58 60%,#4a6540)"></div>
  <div class="photo" role="img" aria-label="Artisan hand painting fine craftwork" style="left:467px;top:1940px;width:260px;height:260px;background:radial-gradient(circle,#9aa4ac,#4c5660 60%,#2f3338)"></div>
  <div class="photo" role="img" aria-label="Aerial view of lakes and marshland" style="left:787px;top:1945px;width:260px;height:260px;background:radial-gradient(circle,#6c8a5a,#4e6d45 55%,#6f94b8)"></div>
  <div class="spot" style="left:123px;top:2242px"><h3>Historical Villages</h3><p>Explore picturesque villages like<br>Mortemart, Turenne, or Saint-Léonard.</p></div>
  <div class="spot" style="left:437px;top:2242px"><h3>Craftsmanship &amp; Markets</h3><p>Meet local producers and artisans that<br>embody regional savoir-faire.</p></div>
  <div class="spot" style="left:757px;top:2247px"><h3>Family Activities</h3><p>Parks, farms, outdoor adventures —<br>perfect for weekend discoveries.</p></div>
</section>

<section class="reviews">
  <h2 class="section-title center" style="top:2426px">What Our Clients Say</h2>
  <p class="lead center" style="top:2492px">Your trust is our priority. Discover the experiences of families and<br>individuals who have chosen Vento Saurelle.</p>
  <span class="divider" role="img" aria-label="Wavy ornamental divider" style="left:552px;top:2566px"></span>

  <svg class="arrow" style="left:84px" width="32" height="26" viewBox="0 0 32 26"><path d="M30 13H3M13 3L3 13l10 10" fill="none" stroke="#263326" stroke-width="2"/></svg>
  <svg class="arrow" style="left:1088px" width="32" height="26" viewBox="0 0 32 26"><path d="M2 13h27M19 3l10 10-10 10" fill="none" stroke="#263326" stroke-width="2"/></svg>

  <article class="review" style="left:162px">
    <span class="q" style="left:-12px;top:-6px">“</span><span class="q" style="right:-8px;bottom:-22px">”</span>
    <div class="stars">★★★★★</div>
    <p>Lorem ipsum dolor sit amet, conse ctetur adipi scing elit, sed do eius mod tempor incididunt ut labore et dolore magna aliqua. Ut enim ad minim veniam, quis nos rucco laboris nisi ut aliqu ip ex ea commodo cons equat.</p>
    <div class="reviewer"><span class="avatar"></span><div><b>Lena Dorval</b><small>2 Days Ago</small></div></div>
  </article>
  <article class="review" style="left:388px">
    <span class="q" style="left:-12px;top:-6px">“</span><span class="q" style="right:-8px;bottom:-22px">”</span>
    <div class="stars">★★★★★</div>
    <p>Lorem ipsum dolor sit amet, conse ctetur adipi scing elit, sed do eius mod tempor incididunt ut labore et dolore magna aliqua. Ut enim ad minim veniam, quis nos rucco laboris nisi ut aliqu ip ex ea commodo cons equat.</p>
    <div class="reviewer"><span class="avatar"></span><div><b>Lena Dorval</b><small>2 Days Ago</small></div></div>
  </article>
  <article class="review" style="left:615px">
    <span class="q" style="left:-12px;top:-6px">“</span><span class="q" style="right:-8px;bottom:-22px">”</span>
    <div class="stars">★★★★★</div>
    <p>Lorem ipsum dolor sit amet, conse ctetur adipi scing elit, sed do eius mod tempor incididunt ut labore et dolore magna aliqua. Ut enim ad minim veniam, quis nos rucco laboris nisi ut aliqu ip ex ea commodo cons equat.</p>
    <div class="reviewer"><span class="avatar"></span><div><b>Lena Dorval</b><small>2 Days Ago</small></div></div>
  </article>
  <article class="review" style="left:845px">
    <span class="q" style="left:-12px;top:-6px">“</span><span class="q" style="right:-8px;bottom:-22px">”</span>
    <div class="stars">★★★★★</div>
    <p>Lorem ipsum dolor sit amet, conse ctetur adipi scing elit, sed do eius mod tempor incididunt ut labore et dolore magna aliqua. Ut enim ad minim veniam, quis nos rucco laboris nisi ut aliqu ip ex ea commodo cons equat.</p>
    <div class="reviewer"><span class="avatar"></span><div><b>Lena Dorval</b><small>2 Days Ago</small></div></div>
  </article>
</section>

<section class="social">
  <div class="abs" style="left:581px;top:3020px;width:38px;height:38px;border-radius:50%;background:var(--ink)"></div>
  <h2 class="section-title center" style="top:3080px">Follow Us on Fernpost</h2>
  <p class="lead center" style="top:3146px">Stay informed about new land opportunities,<br>local news, and life in Limousin.</p>
  <span class="divider" role="img" aria-label="Wavy ornamental divider" style="left:552px;top:3219px"></span>

  <div class="feed">
    <article class="post">
      <div class="post-head"><span class="dot"></span><div><b>VENTO SAURELLE</b> <span class="follow">· Follow</span><br><small>5h</small></div><span class="x">··· ✕</span></div>
      <div class="post-text">Lorem Ipsum is simply dummy text of the printing and typesettin</div>
      <div class="post-photo" role="img" aria-label="Stone village reflected in a river" style="background:linear-gradient(180deg,#b9c7cf,#8a8468 45%,#3f5668)"></div>
      <div class="post-foot">● 34<span style="float:right">4 ● 1 ➦</span><div class="post-actions"><span>Like</span><span>Comment</span><span>Share</span></div></div>
    </article>
    <article class="post">
      <div class="post-head"><span class="dot"></span><div><b>VENTO SAURELLE</b> <span class="follow">· Follow</span><br><small>5h</small></div><span class="x">··· ✕</span></div>
      <div class="post-text">Lorem Ipsum is simply dummy text of the printing and typesettin</div>
      <div class="post-photo" role="img" aria-label="Market stall with pumpkins and onions" style="background:linear-gradient(180deg,#8a4a2e,#d0682c 50%,#7a4a55)"></div>
      <div class="post-foot">● 34<span style="float:right">4 ● 1 ➦</span><div class="post-actions"><span>Like</span><span>Comment</span><span>Share</span></div></div>
    </article>
    <article class="post">
      <div class="post-head"><span class="dot"></span><div><b>VENTO SAURELLE</b> <span class="follow">· Follow</span><br><small>5h</small></div><span class="x">··· ✕</span></div>
      <div class="post-text">Lorem Ipsum is simply dummy text of the printing and typesettin</div>
      <div class="post-photo" role="img" aria-label="Castle on a lake with a tour boat" style="background:linear-gradient(180deg,#6f9bd0,#7d8a5a 50%,#3f6e86)"></div>
      <div class="post-foot">● 34<span style="float:right">4 ● 1 ➦</span><div class="post-actions"><span>Like</span><span>Comment</span><span>Share</span></div></div>
    </article>
  </div>
</section>

<section class="cta">
  <div class="cta-mark"></div>
  <h2>Ready to Take the Next Step?</h2>
  <p>Whether you're planning to relocate, invest, or simply explore possibilities, we<br>are here to help you connect with the land that fits your dreams.</p>
  <a class="btn" style="left:366px;top:370px;width:258px">Book an Appointment</a>
  <a class="btn" style="left:648px;top:370px;width:164px">Contact Us</a>
</section>

<footer>
  <div class="footer-mark"></div>
  <div class="footer-name">VENTO SAURELLE</div>
  <nav class="footer-nav">
    <a style="left:380px">Home</a>
    <a style="left:460px">About Us</a>
    <a style="left:577px">Land Prospecting</a>
    <a style="left:757px">Contact</a>
  </nav>
  <div class="copyright">Copyright © 2025 All Rights Reserved</div>
</footer>

</body>
</html>
```